Under 16 Cricket Tour To Malaysia

I need a flyer to promote an under 16 cricket to Malaysia
The tour will run from April 25th 2108 to May the 7th

Target Market(s)

Boys aged 15-16

Industry/Entity Type

Tour

Font styles to use
Serif

Colors
0255a3
ec1f27

Requirements
Must have
• Dates of the tour
• T20 and Limited Overs games against teams from 5 other countries.
• Name of the tournament is Kestrel Bay International Under 16 Cricket Tournament
• Level 3 coaches with international experience
• Contact Marcus at marcus@pellowfield.com.au for more information.

```html
<!DOCTYPE html>
<html lang="en">
<head>
<meta charset="UTF-8">
<title>Under 16 Cricket Tour to Malaysia</title>
<link href="https://fonts.googleapis.com/css2?family=Anton&family=Montserrat:wght@500;600;700;800&display=swap" rel="stylesheet">
<style>
  :root{
    --page-bg:#e9e6e1;
    --grass:#5fa83a;
    --grass-deep:#3f8a26;
    --grass-light:#8cc63f;
    --paper:#efefed;
    --ink:#111111;
    --ink-soft:#2a2a2a;
    --white:#ffffff;
    --accent-green:#7ab648;
    --banner-green:#3f8f26;
    --brand-blue:#0255a3;
    --brand-red:#ec1f27;
  }
  *{box-sizing:border-box;margin:0;padding:0}
  html,body{width:1200px;height:942px;overflow:hidden;background:var(--page-bg)}
  .flyer{
    position:absolute;left:285px;top:21px;width:629px;height:900px;
    background:var(--paper);overflow:hidden;
    box-shadow:0 4px 14px rgba(0,0,0,.25);
    font-family:"Montserrat",sans-serif;
  }
  .hero-photo{
    position:absolute;left:0;top:0;width:629px;height:480px;
    background:linear-gradient(180deg,#2b3320 0%,#3d4a2c 30%,#5b7a3a 55%,#6fae3c 75%,#5ea336 100%);
  }
  .paper-band{
    position:absolute;left:0;top:462px;width:629px;height:240px;
    background:linear-gradient(180deg,#f3f3f1 0%,#e6e6e3 100%);
  }
  .torn{position:absolute;left:0;width:629px}
  .torn--top{top:440px;height:50px}
  .torn--bottom{top:680px;height:40px}
  .grass-foot{
    position:absolute;left:0;top:712px;width:629px;height:188px;
    background:linear-gradient(180deg,var(--grass-light) 0%,var(--grass) 50%,var(--grass-deep) 100%);
  }
  .headline{
    position:absolute;left:0;top:362px;width:629px;text-align:center;
    font-family:"Anton",sans-serif;font-size:74px;line-height:1;color:var(--ink);
    letter-spacing:1px;
    text-shadow:3px 0 0 #fff,-3px 0 0 #fff,0 3px 0 #fff,0 -3px 0 #fff,2px 2px 0 #fff,-2px -2px 0 #fff,2px -2px 0 #fff,-2px 2px 0 #fff,0 4px 8px rgba(0,0,0,.5);
  }
  .tour-banner{
    position:absolute;left:110px;top:442px;width:394px;height:50px;
    background:linear-gradient(180deg,#4a9a2e,#2f7a1c);
    display:flex;align-items:center;justify-content:center;
    color:var(--white);font-weight:800;font-size:30px;letter-spacing:.5px;
  }
  .date-bar{position:absolute;left:76px;top:498px;width:442px;height:50px}
  .date-bar svg{position:absolute;inset:0}
  .date-text{
    position:absolute;inset:0;display:flex;align-items:center;justify-content:center;gap:7px;
    color:var(--white);font-weight:700;font-size:17px;letter-spacing:.8px;
  }
  .date-text .joiner{color:var(--accent-green)}
  .date-text .year{color:var(--accent-green);font-size:28px;font-weight:800;margin-left:8px}

  .tour-details{
    position:absolute;left:20px;top:556px;width:589px;text-align:center;
    color:var(--ink-soft);font-size:11.5px;font-weight:600;line-height:15px;
  }
  .tour-details__event{
    color:var(--banner-green);font-size:12.5px;font-weight:800;letter-spacing:.4px;
  }
  .tour-details__contact strong{color:var(--brand-blue);font-weight:700}

  .sponsor{position:absolute;display:flex;flex-direction:column;align-items:center;font-weight:800;white-space:nowrap}
  .sponsor--left{left:110px;width:210px;top:630px;gap:2px}
  .sponsor--right{left:318px;width:190px;top:622px;gap:4px}
  .sponsor__name{font-size:20px;color:var(--brand-red);line-height:1}
  .sponsor__sub{font-size:14px;color:#222;font-weight:700;line-height:1.1}
  .sponsor__dot{width:32px;height:32px;border-radius:50%;background:var(--brand-red)}
  .sponsor__label{font-size:13px;color:var(--brand-blue);letter-spacing:.6px;line-height:1}

  .snapshot{
    position:absolute;background:var(--white);padding:8px;
    box-shadow:0 3px 8px rgba(0,0,0,.35);
  }
  .snapshot__image{width:100%;height:100%}
  .snapshot--city{left:16px;top:712px;width:258px;height:160px;transform:rotate(-4deg)}
  .snapshot--city .snapshot__image{background:linear-gradient(160deg,#2a2f5a,#6b4a6f 55%,#c98a4a)}
  .snapshot--batter{left:216px;top:734px;width:188px;height:158px;z-index:2}
  .snapshot--batter .snapshot__image{background:linear-gradient(180deg,#2a2f2a,#8a7a60 60%,#c4ad87)}
  .snapshot--terraces{left:376px;top:718px;width:232px;height:158px;transform:rotate(3deg)}
  .snapshot--terraces .snapshot__image{background:linear-gradient(150deg,#d8e8c0,#7fa83a 50%,#2f5a1e)}
</style>
</head>
<body>
<main class="flyer">
  <div class="hero-photo" role="img" aria-label="Young cricketers on a grass pitch: a batter in a helmet, a wicketkeeper crouched by the stumps and two fielders in whites"></div>
  <div class="paper-band"></div>
  <svg class="torn torn--top" viewBox="0 0 629 50" preserveAspectRatio="none">
    <polygon fill="#f3f3f1" points="0,30 20,24 40,34 60,22 80,32 100,26 120,36 140,28 520,30 540,22 560,34 580,24 600,32 629,26 629,50 0,50"/>
  </svg>
  <svg class="torn torn--bottom" viewBox="0 0 629 40" preserveAspectRatio="none">
    <polygon fill="#8cc63f" points="0,20 18,12 36,22 54,8 72,18 92,10 110,20 130,6 150,16 170,10 190,22 210,8 230,18 250,12 270,22 290,6 310,16 330,10 350,20 370,8 390,18 410,12 430,22 450,6 470,16 490,10 510,20 530,8 550,18 570,12 590,22 610,10 629,16 629,40 0,40"/>
  </svg>
  <div class="grass-foot"></div>

  <h1 class="headline">UNDER 16 CRICKET</h1>
  <div class="tour-banner">TOUR TO MALAYSIA</div>

  <div class="date-bar">
    <svg viewBox="0 0 442 50" preserveAspectRatio="none"><polygon fill="#111" points="22,0 420,0 442,50 0,50"/></svg>
    <p class="date-text"><span>APRIL 25TH</span><span class="joiner">to</span><span>MAY THE 7TH</span><span class="year">2018</span></p>
  </div>

  <div class="tour-details">
    <p class="tour-details__event">KESTREL BAY INTERNATIONAL UNDER 16 CRICKET TOURNAMENT</p>
    <p>T20 and Limited Overs games against teams from 5 other countries</p>
    <p>Level 3 coaches with international experience</p>
    <p class="tour-details__contact">Contact Marcus at <strong>marcus@pellowfield.com.au</strong> for more information</p>
  </div>

  <div class="sponsor sponsor--left">
    <span class="sponsor__name">RIDGELINE SPORT</span>
    <span class="sponsor__sub">HARWICK</span>
  </div>
  <div class="sponsor sponsor--right">
    <span class="sponsor__dot"></span>
    <span class="sponsor__label">PELLOWFIELD SPORTS</span>
  </div>

  <figure class="snapshot snapshot--city"><div class="snapshot__image" role="img" aria-label="Kuala Lumpur city skyline with twin towers at dusk"></div></figure>
  <figure class="snapshot snapshot--terraces"><div class="snapshot__image" role="img" aria-label="Green terraced rice fields in soft morning light"></div></figure>
  <figure class="snapshot snapshot--batter"><div class="snapshot__image" role="img" aria-label="Young batter taking guard on a floodlit pitch"></div></figure>
</main>
</body>
</html>
```